IV Nutritional Clinic Web Design

We are working with Velmo. They are an IV Nutritional Clinic and in need of a new website design.
Some sites to use for inspiration:
https://brantlowcare.example
https://www.zolvarihealth.example
https://www.quellspa.example
https://pimrolift.example
https://www.dorvak-well.example/pages/iv-therapy-west-hollywood
https://www.tqoncowell.example/cancer-care/iv-drips/
https://drelmavita.example
https://salbrikmed.example
Thank you for taking the time to consider designing a website for us. We are web developers based in Stockton, CA, USA. Most of our projects go through the same process. Understanding this process may help you win a project with us. We custom-code all of our websites in-house. We don’t have any requirements as to what tools you use for your design, but we prefer Figma files. For any design that we label as four-stars, we send it to the client for review. The client picks the final design they want us to use. Once we complete this process, we will continue to show additional clients all the four-star sites and purchase them later. Your designs will have multiple chances to sell. For better chances of success, we ask that you follow these guidelines.
IMAGES:
If you use any images or icons in the design, we ask that you have a link to the asset so we can purchase the image/icon. Most of the designs we submit do not have the customer’s images on them unless they have some great images. Be creative; show us the feeling you are trying to portray with your image choices. Use any royalty-free site you choose. We subscribe to Corvix and mainly use their images, but we can purchase images outside of Corvix.
PLEASE NOTE: we will not submit designs to clients with watermarks on the images.
FONTS:
We ask that you identify the fonts used in the design. This can be done in a message if you want. We typically use Lumen Typeset and Corvix Fonts.
CONTENT:
We're always open to different content and ideas. We often submit designs with stock images so the client can see our vision. We typically take pictures after the website launch to use their images with our vision. Lorem Ipsum is fine for paragraphs, but we ask that you write the headers in correct English. We want to be able to show the vision and identify the sections of the website.
INSPIRATION:
We typically add a couple of links in the brief of websites we like to help you get started in your design.
REVISIONS:
We do not often ask for revisions of the designs unless we see something in the design that may not appeal to the client. If there are slight changes that we want to make, we do that in the development process.
FEEDBACK:
We rarely give feedback on designs during the design process. We are working on many website projects and do not have the time to provide feedback. We usually respond if your request is well thought out and asks specific questions, but a note asking “feedback, please” usually goes unanswered.
Number of Pages Required
1 page
Look and feel
Each slider illustrates characteristics of the customer's brand and the style your logo design should communicate.

```html
<!DOCTYPE html>
<html lang="en">
<head>
<meta charset="utf-8">
<title>Velmo IV Therapy</title>
<link rel="stylesheet" href="https://fonts.googleapis.com/css2?family=Red+Hat+Display:wght@500;700;800;900&family=Lato:wght@400;700&display=swap">
<style>
:root{
  --stage:#b3b3b3;
  --navy:#1d2f8f;
  --blue:#2f4aa3;
  --blue-deep:#243d93;
  --green:#8cb253;
  --ink:#161616;
  --muted:#4a4a4a;
  --paper:#ffffff;
  --mist:#d7d7d7;
  --night:#1c1c1e;
  --head:"Red Hat Display",sans-serif;
  --body:"Lato",sans-serif;
}
*{margin:0;padding:0;box-sizing:border-box}
html,body{width:1200px;height:2656px;overflow:hidden;background:var(--stage)}
body{font-family:var(--body);color:var(--ink)}
.page{position:absolute;left:79px;top:69px;width:1041px;height:2517px;background:var(--paper);box-shadow:0 10px 40px rgba(0,0,0,.25);overflow:hidden}
section,footer{position:relative;width:100%}
.abs{position:absolute}
.btn{position:absolute;display:flex;align-items:center;justify-content:center;font-family:var(--head);font-weight:800;font-size:10px;letter-spacing:.2px;text-transform:uppercase;color:#fff}
.btn-green{background:var(--green)}
.btn-navy{background:var(--navy)}
.btn-outline{border:2px solid #fff}
h2{font-family:var(--head);font-weight:800;font-size:25px;color:var(--ink)}

/* hero */
.hero{height:500px;background:linear-gradient(90deg,#234a86 0%,#3e6595 35%,#8aa1b4 65%,#a7b3bc 100%)}
.hero-photo{position:absolute;inset:0;background:radial-gradient(ellipse at 72% 45%,rgba(60,70,80,.35),transparent 45%),linear-gradient(180deg,transparent 60%,rgba(70,60,50,.35))}
.logo{left:168px;top:16px;display:flex;align-items:center;gap:6px;font-family:var(--head);font-weight:800;font-size:24px;color:#fff}
.logo i{width:9px;height:9px;background:var(--green);display:block}
.nav{top:25px;left:466px;display:flex;gap:0;font-family:var(--head);font-weight:700;font-size:10px;color:#fff}
.nav a{position:absolute;white-space:nowrap;color:#fff;text-decoration:none}
.nav a.on{color:var(--green)}
.hero h1{left:168px;top:189px;font-family:var(--head);font-weight:900;font-size:33px;line-height:38px;color:#fff}
.hero p{left:168px;top:278px;width:390px;font-size:9.6px;line-height:17px;color:#fff}
.counter{left:804px;top:404px;font-family:var(--head);font-weight:800;font-size:33px;color:#fff}
.counter small{font-size:19px}

/* why */
.why{height:610px}
.why h2{position:absolute;top:54px;width:100%;text-align:center}
.track{left:212px;top:185px;width:616px;border-top:1px dashed #888}
.dot{width:8px;height:8px;border-radius:50%;background:var(--navy);top:182px}
.card{position:absolute;top:107px;width:110px;height:144px;background:#fff;box-shadow:0 6px 22px rgba(0,0,0,.12);text-align:center}
.card svg{position:absolute;left:33px;top:18px}
.card .node{position:absolute;left:50px;top:79px;width:1px;height:12px;border-left:1px dashed #888}
.card .ring{position:absolute;left:46px;top:91px;width:9px;height:9px;border:1px solid #888;border-radius:50%}
.card b{position:absolute;left:0;right:0;top:116px;font-family:var(--head);font-weight:800;font-size:10.5px}
.who-photo{left:230px;top:307px;width:271px;height:355px;background:linear-gradient(135deg,#e7e9ec,#b9c3d2 55%,#6a7fa5);z-index:3}
.who h3{position:absolute;left:545px;top:343px;font-family:var(--head);font-weight:800;font-size:25px}
.who p{position:absolute;left:545px;top:376px;width:282px;font-size:9.2px;line-height:14px;color:var(--muted)}

/* services */
.services{height:367px;background:var(--blue)}
.services-bg{position:absolute;inset:0;background:linear-gradient(180deg,rgba(20,40,110,.0),rgba(20,40,110,.25)),radial-gradient(ellipse at 50% 20%,#4a62ae,transparent 60%)}
.services h2{position:absolute;left:168px;top:94px;color:#fff}
.grid{left:156px;top:144px;width:731px;height:192px}
.cell{position:absolute;width:176px;height:96px;display:flex;align-items:center;gap:12px;padding-left:26px;font-family:var(--head);font-weight:800;font-size:10.5px;line-height:13px;color:#fff}
.cell.v{border-right:1px solid rgba(255,255,255,.25)}
.cell.h{border-bottom:1px solid rgba(255,255,255,.25)}
.cell.hi{background:var(--green);flex-direction:column;align-items:flex-start;justify-content:flex-end;gap:2px;padding:0 16px 12px}
.cell.hi span{font-family:var(--body);font-weight:400;font-size:9px;line-height:14px}
.hi-icon{left:537px;top:123px;width:42px;height:42px;background:#fff;display:flex;align-items:center;justify-content:center;z-index:2}

/* functionality */
.func{height:442px}
.func h2{position:absolute;top:50px;width:100%;text-align:center}
.tile{position:absolute;top:93px;width:226px;height:252px}
.tile .ph{position:absolute;inset:0}
.tile .shade{position:absolute;inset:0;background:linear-gradient(180deg,transparent 55%,rgba(0,0,0,.55))}
.tile .cap{position:absolute;left:19px;top:191px;width:195px;color:#fff;font-size:9px;line-height:14px}
.tile .cap b{font-family:var(--head);font-weight:800;font-size:10px;display:block;margin-bottom:2px}
.tile .go{position:absolute;left:181px;top:239px;width:26px;height:26px;background:var(--green);display:flex;align-items:center;justify-content:center}
.view{top:377px;width:100%;text-align:center;font-family:var(--head);font-weight:800;font-size:10px}
.view span{border-bottom:1px solid var(--ink);padding-bottom:1px}

/* testimonials */
.testi{height:331px;background:var(--mist)}
.testi-photo{left:521px;top:0;width:520px;height:331px;background:linear-gradient(120deg,#cfd5dc,#9aa6b3 50%,#e4e6e8)}
.testi h2{position:absolute;left:168px;top:60px}
.stars{left:168px;top:100px;color:#f2c200;font-size:16px;letter-spacing:1px}
.testi p{position:absolute;left:168px;top:124px;width:300px;font-size:9.2px;line-height:17px;color:var(--muted)}
.avatar{left:168px;top:194px;width:39px;height:39px;border-radius:50%;background:linear-gradient(135deg,#e7795a,#b94b3a)}
.who-name{left:220px;top:200px;font-size:10px;line-height:12px}
.who-name b{font-family:var(--head);font-weight:800}
.arrows{left:168px;top:251px}

/* footer */
footer{height:266px;background:var(--night);color:#fff}
.fcol{position:absolute;top:56px;font-size:9.5px;line-height:18.5px}
.fcol h4{font-family:var(--head);font-weight:800;font-size:11.5px;color:var(--green);margin-bottom:12px;line-height:14px}
.fcol b{font-family:var(--head);font-weight:800;font-size:9.5px;display:block;line-height:12px}
.fcol .blk{line-height:11px;margin-bottom:9px}
.field{left:684px;top:106px;width:188px;height:33px;background:#2c2c2e;display:flex;align-items:center;justify-content:space-between;padding:0 12px;font-size:9px;color:#9a9a9a}
.rule{left:168px;top:228px;width:704px;border-top:1px solid #3a3a3c}
.top-btn{left:883px;top:211px;width:33px;height:33px;background:var(--navy);display:flex;align-items:center;justify-content:center}
.copy{top:242px;width:100%;text-align:center;font-size:9px}
</style>
</head>
<body>
<div class="page">

  <section class="hero">
    <div class="hero-photo" role="img" aria-label="Woman holding a standing yoga pose on seaside rocks"></div>
    <div class="abs logo"><span>VELMO</span><i></i></div>
    <nav class="abs nav">
      <a class="on" style="left:0">Home</a>
      <a style="left:46px">About Us</a>
      <a style="left:108px">Services</a>
      <a style="left:165px">Project</a>
      <a style="left:215px">Testimonials</a>
    </nav>
    <a class="btn btn-navy" style="left:765px;top:14px;width:107px;height:33px">Get Started</a>
    <h1 class="abs">"Revitalize Your Body<br>With Iv Nutrient Therapy"</h1>
    <p class="abs">Short benefit-driven statement, e.g., "Boost immunity, hydrate instantly, and increase energy with our custom IV drips."</p>
    <a class="btn btn-green" style="left:168px;top:320px;width:116px;height:34px">Explore Services</a>
    <a class="btn btn-outline" style="left:302px;top:320px;width:91px;height:34px">Contact Us</a>
    <div class="abs counter">01/<small>03</small></div>
  </section>

  <section class="why">
    <h2>Why Choose Velmo Iv Therapy?</h2>
    <div class="abs track"></div>
    <div class="abs dot" style="left:208px"></div>
    <div class="abs dot" style="left:824px"></div>
    <div class="card" style="left:255px">
      <svg width="44" height="44" viewBox="0 0 44 44" fill="none" stroke="#1d2f8f" stroke-width="1.6"><circle cx="22" cy="20" r="10"/><path d="M22 13l2 5h5l-4 3 2 5-5-3-5 3 2-5-4-3h5z"/><path d="M22 30v10M8 10v14M36 10v14"/></svg>
      <span class="node"></span><span class="ring"></span><b>Fast Hydration</b>
    </div>
    <div class="card" style="left:395px">
      <svg width="44" height="44" viewBox="0 0 44 44" fill="none" stroke="#1d2f8f" stroke-width="1.6"><rect x="6" y="14" width="26" height="22" rx="2"/><circle cx="30" cy="12" r="7"/><path d="M30 9v3l2 2M12 22h14M12 28h10"/></svg>
      <span class="node"></span><span class="ring"></span><b>Fast Hydration</b>
    </div>
    <div class="card" style="left:535px">
      <svg width="44" height="44" viewBox="0 0 44 44" fill="none" stroke="#1d2f8f" stroke-width="1.6"><circle cx="18" cy="18" r="11"/><circle cx="18" cy="16" r="4"/><path d="M11 25c2-4 12-4 14 0"/><circle cx="32" cy="31" r="7"/></svg>
      <span class="node"></span><span class="ring"></span><b>Fast Hydration</b>
    </div>
    <div class="card" style="left:675px">
      <svg width="44" height="44" viewBox="0 0 44 44" fill="none" stroke="#1d2f8f" stroke-width="1.6"><circle cx="22" cy="20" r="14"/><circle cx="22" cy="18" r="5"/><path d="M14 29c3-5 13-5 16 0"/><circle cx="32" cy="32" r="5"/></svg>
      <span class="node"></span><span class="ring"></span><b>Fast Hydration</b>
    </div>
    <div class="abs who-photo" role="img" aria-label="Clinician adjusting an IV drip bag on a stand"></div>
    <div class="who">
      <h3>Who We Are Velmo</h3>
      <p>Lorem ipsum dolor sit amet, consectetuer adipiscing elit, sed diam nonummy nibh euismod tincidunt ut laoreet dolore magna aliquam erat volutpat. Ut wisi enim ad minim veniam, quis nostrud exerci tation ullamcorper suscipit.</p>
      <a class="btn btn-green" style="left:545px;top:455px;width:95px;height:33px">Read More</a>
    </div>
  </section>

  <section class="services">
    <div class="services-bg" role="img" aria-label="Aerial city skyline tinted blue"></div>
    <h2>Our Services</h2>
    <a class="btn btn-green" style="left:778px;top:93px;width:94px;height:33px">Read More</a>
    <div class="abs hi-icon"><svg width="30" height="30" viewBox="0 0 30 30" fill="none" stroke="#222" stroke-width="1.4"><rect x="4" y="12" width="14" height="12"/><circle cx="22" cy="12" r="5"/><path d="M4 26h22M8 8l4-4 4 4"/></svg></div>
    <div class="abs grid">
      <div class="cell v h" style="left:0;top:0"><svg width="36" height="36" viewBox="0 0 36 36" fill="none" stroke="#fff" stroke-width="1.5"><circle cx="16" cy="18" r="12"/><rect x="12" y="16" width="16" height="10"/><circle cx="15" cy="28" r="2"/><circle cx="25" cy="28" r="2"/></svg>Boosts Energy</div>
      <div class="cell v h" style="left:176px;top:0"><svg width="36" height="36" viewBox="0 0 36 36" fill="none" stroke="#fff" stroke-width="1.5"><circle cx="10" cy="18" r="5"/><path d="M3 32c1-6 13-6 14 0"/><path d="M24 8l8 3v7c0 6-4 9-8 11-4-2-8-5-8-11v-7z"/></svg>Strengthens<br>Immunity</div>
      <div class="cell hi" style="left:352px;top:0">Improves Skin Glow<span>Lorem ipsum dolor sit amet, consectetuer adipiscing elit, sed diam nonummy.</span></div>
      <div class="cell h" style="left:528px;top:0"><svg width="36" height="36" viewBox="0 0 36 36" fill="none" stroke="#fff" stroke-width="1.5"><circle cx="18" cy="20" r="12"/><path d="M10 14c4 4 12 4 16 0M18 8v24"/><circle cx="28" cy="8" r="3"/></svg>Enhances Athletic<br>Recovery</div>
      <div class="cell v" style="left:0;top:96px"><svg width="36" height="36" viewBox="0 0 36 36" fill="none" stroke="#fff" stroke-width="1.5"><rect x="3" y="14" width="20" height="14"/><path d="M23 18h7l3 5v5H23"/><circle cx="9" cy="30" r="2"/><circle cx="27" cy="30" r="2"/><circle cx="28" cy="8" r="5"/></svg>Boosts Energy</div>
      <div class="cell v" style="left:176px;top:96px"><svg width="36" height="36" viewBox="0 0 36 36" fill="none" stroke="#fff" stroke-width="1.5"><rect x="10" y="6" width="18" height="22"/><path d="M14 12h10M14 17h10"/><rect x="3" y="22" width="10" height="10"/></svg>Strengthens<br>Immunity</div>
      <div class="cell v" style="left:352px;top:96px"><svg width="36" height="36" viewBox="0 0 36 36" fill="none" stroke="#fff" stroke-width="1.5"><path d="M18 4l6 2v5c0 4-3 6-6 7-3-1-6-3-6-7V6z"/><circle cx="9" cy="26" r="5"/><circle cx="27" cy="26" r="5"/><path d="M2 26h32"/></svg>Improves Skin<br>Glow</div>
      <div class="cell" style="left:528px;top:96px"><svg width="36" height="36" viewBox="0 0 36 36" fill="none" stroke="#fff" stroke-width="1.5"><path d="M6 18a12 12 0 0 1 24 0z"/><path d="M18 6v26"/><circle cx="9" cy="28" r="4"/><circle cx="27" cy="28" r="4"/></svg>Enhances Athletic<br>Recovery</div>
    </div>
  </section>

  <section class="func">
    <h2>Functionality Requirements</h2>
    <div class="tile" style="left:168px">
      <div class="ph" role="img" aria-label="Two clinic staff reviewing a tablet together" style="background:linear-gradient(150deg,#ece9f0,#c9c3cf 50%,#8f8a93)"></div>
      <div class="shade"></div>
      <div class="cap"><b>Responsive Design:</b>Ensure the site is mobile-friendly and optimized for all devices.</div>
      <div class="go"><svg width="10" height="10" viewBox="0 0 10 10" fill="none" stroke="#fff" stroke-width="2"><path d="M3 1l4 4-4 4"/></svg></div>
    </div>
    <div class="tile" style="left:407px">
      <div class="ph" role="img" aria-label="Gloved hands preparing an injection syringe" style="background:linear-gradient(150deg,#f1efee,#d8d2cd 55%,#8e8783)"></div>
      <div class="shade"></div>
      <div class="cap"><b>Rater Tool Integration:</b>Seamlessly embed the rater tool (provided by the other team) into the landing page.</div>
      <div class="go"><svg width="10" height="10" viewBox="0 0 10 10" fill="none" stroke="#fff" stroke-width="2"><path d="M3 1l4 4-4 4"/></svg></div>
    </div>
    <div class="tile" style="left:646px">
      <div class="ph" role="img" aria-label="Nurse preparing a patient's arm for an IV line" style="background:linear-gradient(150deg,#dfe3e7,#a8b2bc 55%,#6f7780)"></div>
      <div class="shade"></div>
      <div class="cap"><b>Fast Loading Times:</b>Optimize images and code for quick load times.</div>
      <div class="go"><svg width="10" height="10" viewBox="0 0 10 10" fill="none" stroke="#fff" stroke-width="2"><path d="M3 1l4 4-4 4"/></svg></div>
    </div>
    <div class="abs view"><span>VIEW ALL PROJECT</span></div>
  </section>

  <section class="testi">
    <div class="abs testi-photo" role="img" aria-label="Nurse fitting an IV line to a patient's arm"></div>
    <h2>Testimonials</h2>
    <div class="abs stars">★★★★★</div>
    <p>Lorem ipsum dolor sit amet, consectetuer adipiscing elit, sed diam nonummy nibh euismod tincidunt ut laoreet dolore magna aliquam erat volutpat.</p>
    <div class="abs avatar" role="img" aria-label="Client portrait"></div>
    <div class="abs who-name"><b>Marco T.</b><br>Project Manger</div>
    <svg class="abs arrows" width="52" height="14" viewBox="0 0 52 14" fill="none" stroke-width="1.4"><path d="M12 7H1M5 3L1 7l4 4" stroke="#333"/><path d="M26 7h22M44 2l5 5-5 5" stroke="#1d2f8f"/></svg>
  </section>

  <footer>
    <div class="fcol" style="left:168px"><h4>Why Choose Us</h4>Home<br>About Us<br>Services<br>Project<br>Testimonials</div>
    <div class="fcol" style="left:329px"><h4>Information</h4>Privacy Policy<br>Disclaimer<br>Terms &amp; Candition<br>Site Map</div>
    <div class="fcol" style="left:480px"><h4>Contact Us</h4>
      <div class="blk"><b>PHONE</b>(808)555-0172</div>
      <div class="blk"><b>EMAIL</b>hello@velmo.example</div>
      <div class="blk"><b>ADDRESS</b>218 Kelani Way Ste 310<br>Honolulu, HI 96814</div>
    </div>
    <div class="fcol" style="left:684px"><h4>Newsletter</h4>Subscribe to our newsletter</div>
    <div class="abs field"><span>Enter email address</span><svg width="12" height="12" viewBox="0 0 12 12" fill="#fff"><path d="M11 1L1 5l4 1.5L6.5 11z"/></svg></div>
    <div class="abs rule"></div>
    <div class="abs top-btn"><svg width="10" height="10" viewBox="0 0 10 10" fill="none" stroke="#fff" stroke-width="1.6"><path d="M2 7l3-3 3 3"/></svg></div>
    <div class="abs copy">Copyright © 2024 Harlow Bend Partners, LLC All rights reserved | Privacy and cookie policy Terms | Privacy | Cookies</div>
  </footer>

</div>
</body>
</html>
```